Meridale Crest Advisors – Franchise Growth & Development Presentation

Meridale Crest Advisors is an outsourced franchise sales organization (FSO) that helps franchisors grow their franchise systems without the expense and risk of hiring an internal franchise development team.

We are seeking a professional PowerPoint presentation that will be used to present our services to franchisors, franchise executives, founders, and growth-stage franchise brands.

The presentation should communicate the value of partnering with Meridale Crest Advisors, including:

• Fractional franchise sales team versus hiring internal staff
• 30+ years of franchise industry experience
• 550+ franchise sales successes
• Immediate access to established franchise broker relationships
• Proven franchise development processes
• Franchise growth strategy and enterprise value creation
• Potential private equity and exit opportunities through franchise expansion

The presentation should feel like a modern consulting, investment, or growth strategy presentation rather than a typical sales brochure. We want strong visual storytelling, custom infographics, professional diagrams, and clean business-oriented design.

The audience includes business owners, franchise founders, franchise executives, and investors who are evaluating growth strategies for their franchise systems.

Target Market(s)

Primary Audience: Emerging franchisors Growth-stage franchise brands Franchise founders Franchise CEOs Franchise presidents Franchise development executives Secondary Audience: Private equity firms Franchise investors Strategic buyers Franchise consultants

Industry/Entity Type

Franchise Development, Private Equity / Business Expansion

Font styles to use
Other font styles liked:
• Use Montserrat for titles and Open Sans for body text.

Requirements
Must have
• Modern professional business design Consistent branding throughout Custom infographics Comparison graphics Broker network ecosystem graphic Enterprise value graphic Easy-to-read charts and visuals Editable PowerPoint format Professional iconography. www.meridalecrestadvisors.example as reference for colors
Nice to have
• Franchise-related imagery Subtle growth-themed visuals Timeline graphics Data visualization Private equity / valuation style graphics
Should not have
• Cartoon graphics Clip art Overly busy slides Stock-template appearance Bright neon colors Handwritten fonts Excessive text on slides Juvenile or playful design elements

```html
<!DOCTYPE html>
<html lang="en">
<head>
<meta charset="UTF-8">
<title>Our Process – Meridale Crest Advisors</title>
<link href="https://fonts.googleapis.com/css2?family=Montserrat:wght@600;700&family=Open+Sans:wght@400;600&display=swap" rel="stylesheet">
<style>
  :root {
    --bg: #f5f6fa;
    --navy: #16213e;
    --gold: #b8863b;
    --gold-light: #d6ab55;
    --body: #5b6579;
    --line: #dfe2ea;
    --card: #ffffff;
    --card-border: #e3e6ee;
    --footer: #5d6a80;
  }
  * { margin: 0; padding: 0; box-sizing: border-box; }
  html, body { width: 1200px; height: 675px; overflow: hidden; background: var(--bg); }
  .slide { position: relative; width: 1200px; height: 675px; background: var(--bg); font-family: "Open Sans", Arial, sans-serif; }
  .eyebrow { position: absolute; left: 54px; top: 45px; font-family: "Montserrat", Arial, sans-serif; font-weight: 700; font-size: 15px; letter-spacing: 2.4px; color: var(--gold); }
  .title { position: absolute; left: 54px; top: 77px; font-family: "Montserrat", Arial, sans-serif; font-weight: 700; font-size: 34px; line-height: 36px; color: var(--navy); }
  .track { position: absolute; left: 75px; top: 230px; width: 1061px; height: 3px; background: var(--line); border-radius: 2px; }
  .step-num { position: absolute; top: 211px; width: 42px; height: 42px; border-radius: 50%; background: var(--navy); color: var(--gold-light); font-family: "Montserrat", Arial, sans-serif; font-weight: 700; font-size: 15px; display: flex; align-items: center; justify-content: center; }
  .card { position: absolute; top: 280px; width: 173px; height: 270px; background: var(--card); border: 1px solid var(--card-border); border-radius: 5px; box-shadow: 0 2px 4px rgba(22,33,62,0.06); }
  .card-icon { position: absolute; left: 14px; top: 19px; width: 36px; height: 36px; }
  .card-title { position: absolute; left: 14px; top: 69px; font-family: "Montserrat", Arial, sans-serif; font-weight: 600; font-size: 14px; line-height: 19px; color: var(--navy); }
  .card-body { position: absolute; left: 14px; right: 12px; top: 150px; height: 76px; display: flex; align-items: center; font-size: 11.5px; line-height: 17px; color: var(--body); }
  .footer-brand { position: absolute; left: 45px; top: 651px; font-size: 10px; letter-spacing: 2px; color: var(--footer); text-transform: uppercase; }
  .page-num { position: absolute; right: 39px; top: 651px; font-size: 10px; color: var(--footer); }
</style>
</head>
<body>
<div class="slide">
  <div class="eyebrow">OUR PROCESS</div>
  <h1 class="title">A Proven, Repeatable Franchise<br>Development Process</h1>

  <div class="track"></div>
  <div class="step-num" style="left:54px">01</div>
  <div class="step-num" style="left:239px">02</div>
  <div class="step-num" style="left:424px">03</div>
  <div class="step-num" style="left:610px">04</div>
  <div class="step-num" style="left:796px">05</div>
  <div class="step-num" style="left:980px">06</div>

  <div class="card" style="left:55px">
    <svg class="card-icon" viewBox="0 0 36 36" fill="none" stroke="#16213e" stroke-width="4"><circle cx="18" cy="18" r="15"/><circle cx="18" cy="18" r="7"/><circle cx="18" cy="18" r="1.5" fill="#16213e"/></svg>
    <div class="card-title">Discovery &amp;<br>Strategy</div>
    <div class="card-body">Align on growth goals, ideal candidate profile, and territory priorities.</div>
  </div>

  <div class="card" style="left:240px">
    <svg class="card-icon" viewBox="0 0 36 36" fill="none" stroke="#16213e"><circle cx="14" cy="14" r="10" stroke-width="5"/><line x1="22" y1="22" x2="32" y2="32" stroke-width="6" stroke-linecap="round"/></svg>
    <div class="card-title">Lead<br>Generation</div>
    <div class="card-body">Activate targeted marketing and broker channels to fill the pipeline.</div>
  </div>

  <div class="card" style="left:426px">
    <svg class="card-icon" viewBox="0 0 36 36"><path d="M1 2h34l-13 15v16l-8-5V17z" fill="#16213e" stroke="#16213e" stroke-width="2" stroke-linejoin="round"/></svg>
    <div class="card-title">Candidate<br>Qualification</div>
    <div class="card-body">Vet financial readiness, fit, and motivation before advancing.</div>
  </div>

  <div class="card" style="left:611px">
    <svg class="card-icon" viewBox="0 0 36 36"><rect x="5" y="5" width="26" height="30" rx="3" fill="#16213e"/><rect x="12" y="1" width="12" height="7" rx="2" fill="#16213e" stroke="#fff" stroke-width="1.5"/><path d="M11 20l5 5 9-9" fill="none" stroke="#fff" stroke-width="3.5" stroke-linecap="round" stroke-linejoin="round"/></svg>
    <div class="card-title">Discovery Day &amp;<br>Validation</div>
    <div class="card-body">Coordinate immersive candidate experiences that drive conviction.</div>
  </div>

  <div class="card" style="left:797px">
    <svg class="card-icon" viewBox="0 0 36 36"><path d="M6 1h16l9 9v25H6z" fill="#16213e"/><path d="M22 1v9h9" fill="#fff" opacity="0.35"/><line x1="10" y1="8" x2="17" y2="8" stroke="#fff" stroke-width="2"/><line x1="10" y1="13" x2="17" y2="13" stroke="#fff" stroke-width="2"/><path d="M10 28l3-5 2 6 3-4 2 3h6" fill="none" stroke="#fff" stroke-width="1.6" stroke-linejoin="round"/></svg>
    <div class="card-title">Awarding &amp;<br>Closing</div>
    <div class="card-body">Manage FDD delivery, disclosure timing, and franchise agreement execution.</div>
  </div>

  <div class="card" style="left:982px">
    <svg class="card-icon" viewBox="0 0 36 36"><rect x="1" y="12" width="5" height="12" rx="1" fill="#16213e"/><rect x="30" y="12" width="5" height="12" rx="1" fill="#16213e"/><path d="M6 13l6-3h5l-5 5 3 3 6-5 9 9-3 3-9 3-5-3-7-6z" fill="#16213e"/><path d="M17 10l5 0 8 3v10" fill="none" stroke="#16213e" stroke-width="3"/></svg>
    <div class="card-title">Post-Sale<br>Handoff</div>
    <div class="card-body">Transition new franchisees smoothly into onboarding and operations.</div>
  </div>

  <div class="footer-brand">Meridale Crest Advisors</div>
  <div class="page-num">06</div>
</div>
</body>
</html>
```